Business cards, envelopes and letterhead
Simple but professional
Business cards, envelopes and letterhead -
Creative Brief
Professional
Martin Doyle
President & CEO
4273 Beldon Street Chilliwack, BC V4K 7N2 Canada
mdoyle@fernobrix.com
www.fernobrix.com
On the back, we want at least the logo (maybe the styled water drop only, we might not need the "FERNOBRIX" there but that's up to the designer), and we want to have a lot of white space so people can make notes on this when decided (though we don't need lines on the back for writing or so).

```html
<!DOCTYPE html>
<html lang="en">
<head>
<meta charset="utf-8">
<title>Fernobrix Envelope</title>
<link href="https://fonts.googleapis.com/css2?family=Roboto+Condensed:wght@400;700&display=swap" rel="stylesheet">
<style>
  :root {
    --page-bg: #ffffff;
    --paper: #ffffff;
    --edge: #3a3a3a;
    --brand-navy: #1d4f91;
    --brand-cyan: #2cb8ea;
    --brand-mid: #1f8fd0;
    --brand-deep: #183f8c;
    --text-grey: #4a5a70;
    --window: #7b7b7b;
  }
  html, body {
    margin: 0;
    padding: 0;
    width: 1200px;
    height: 871px;
    overflow: hidden;
    background: var(--page-bg);
  }
  .envelope {
    position: absolute;
    left: 91px;
    top: 175px;
    width: 1020px;
    height: 463px;
    background: var(--paper);
    border: 1.5px solid var(--edge);
    box-sizing: border-box;
    overflow: hidden;
    font-family: "Roboto Condensed", sans-serif;
  }
  .side-band {
    position: absolute;
    left: 0;
    top: 0;
    width: 1020px;
    height: 463px;
  }
  .return-address {
    position: absolute;
    left: 98px;
    top: 40px;
  }
  .brand-name {
    display: flex;
    align-items: center;
    gap: 8px;
    font-size: 29px;
    font-weight: 700;
    color: var(--brand-navy);
    letter-spacing: 0.5px;
    line-height: 1;
  }
  .brand-dot {
    width: 14px;
    height: 14px;
    border-radius: 50%;
    background: var(--brand-navy);
  }
  .address-lines {
    margin-top: 6px;
    font-size: 12px;
    line-height: 16px;
    color: var(--text-grey);
  }
  .address-window {
    position: absolute;
    left: 100px;
    top: 281px;
    width: 389px;
    height: 110px;
    border-radius: 18px;
    background: var(--window);
  }
</style>
</head>
<body>
  <div class="envelope">
    <svg class="side-band" viewBox="0 0 1020 463" aria-hidden="true">
      <defs>
        <linearGradient id="bandFill" x1="0" y1="0" x2="0" y2="1">
          <stop offset="0" stop-color="var(--brand-cyan)"/>
          <stop offset="0.45" stop-color="var(--brand-mid)"/>
          <stop offset="1" stop-color="var(--brand-deep)"/>
        </linearGradient>
      </defs>
      <path d="M0 0 H52 C28 130 38 300 95 463 H0 Z" fill="url(#bandFill)"/>
    </svg>

    <div class="return-address">
      <div class="brand-name"><span class="brand-dot"></span>FERNOBRIX</div>
      <div class="address-lines">
        4273 Beldon Street, Chilliwack, BC<br>
        V4K 7N2 Canada
      </div>
    </div>

    <div class="address-window"></div>
  </div>
</body>
</html>
```